Business card for plumber

I need a business card for my plumbing company.
on it should:
Surname
position
E-mail
Telephone & mobile phone
Website
Please everything as placeholders / fantasy names.
We stand for high quality, hygiene and professionalism.

Colours:
# 606060 anthracite
# f7931e orange
# 2b89cc blue

Industry/Entity Type

Plumber

Contact Information for Business Card

folgt...

```html
<!DOCTYPE html>
<html lang="en">
<head>
<meta charset="utf-8">
<title>Brunnvoll Haustechnik – Business Card</title>
<link rel="stylesheet" href="https://fonts.googleapis.com/css2?family=Roboto:wght@400;700;900&display=swap">
<style>
  :root {
    --page-bg: #2a2a2a;
    --card-bg: #1c1c1c;
    --blue: #2b89cc;
    --orange: #f7931e;
    --anthracite: #606060;
    --text-light: #f2f2f2;
  }
  * { box-sizing: border-box; margin: 0; padding: 0; }
  html, body {
    width: 1200px; height: 900px; overflow: hidden;
    background: var(--page-bg);
    font-family: "Roboto", Arial, sans-serif;
  }
  .stage {
    width: 1200px; height: 900px;
    display: flex; flex-direction: column; align-items: center; justify-content: center; gap: 30px;
  }
  .card {
    width: 700px; height: 400px;
    background: var(--card-bg);
    box-shadow: 0 10px 30px rgba(0,0,0,.45);
    position: relative;
  }
  .card-front { display: flex; align-items: center; padding: 0 50px; }
  .brand { width: 300px; display: flex; align-items: center; gap: 14px; }
  .brand-dot { width: 22px; height: 22px; border-radius: 50%; background: var(--orange); flex: none; }
  .brand-name {
    color: var(--blue); font-weight: 900; font-size: 27px; line-height: 1.1;
    text-transform: uppercase; letter-spacing: .5px;
  }
  .divider { width: 2px; height: 200px; background: var(--blue); margin: 0 34px 0 10px; }
  .contact { color: var(--text-light); font-size: 15px; line-height: 1.45; }
  .person-name { color: var(--blue); font-weight: 900; font-size: 24px; text-transform: uppercase; line-height: 1.1; }
  .person-role { font-size: 16px; margin-bottom: 8px; }
  .address { margin-bottom: 4px; }
  .contact-line { display: flex; align-items: center; gap: 8px; }
  .contact-line svg { width: 13px; height: 13px; flex: none; fill: var(--orange); }
  .card-back { display: flex; align-items: center; justify-content: center; }
  .card-back .brand { width: auto; }
</style>
</head>
<body>
<main class="stage">
  <section class="card card-front">
    <div class="brand">
      <span class="brand-dot"></span>
      <span class="brand-name">Brunnvoll<br>Haustechnik</span>
    </div>
    <div class="divider"></div>
    <div class="contact">
      <p class="person-name">Dario Kessler</p>
      <p class="person-role">President</p>
      <p class="address">2750 N. Linden Street<br>Marlow, IL 60512</p>
      <p class="contact-line">
        <svg viewBox="0 0 24 24"><path d="M6.6 10.8a15 15 0 0 0 6.6 6.6l2.2-2.2a1 1 0 0 1 1-.25 11.4 11.4 0 0 0 3.6.6 1 1 0 0 1 1 1V20a1 1 0 0 1-1 1A17 17 0 0 1 3 4a1 1 0 0 1 1-1h3.5a1 1 0 0 1 1 1c0 1.25.2 2.45.6 3.6a1 1 0 0 1-.25 1z"/></svg>
        (312) 555-0147
      </p>
      <p class="contact-line">
        <svg viewBox="0 0 24 24"><path d="M7 1h10a2 2 0 0 1 2 2v18a2 2 0 0 1-2 2H7a2 2 0 0 1-2-2V3a2 2 0 0 1 2-2zm0 3v14h10V4zm5 15.5a1 1 0 1 0 0 2 1 1 0 0 0 0-2z"/></svg>
        (708) 555-0192 Ext. 305
      </p>
      <p class="contact-line">
        <svg viewBox="0 0 24 24"><path d="M2 5h20v14H2zm2 2v.5l8 5 8-5V7zm0 2.8V17h16V9.8l-8 5z"/></svg>
        info@brunnvollhaustechnik.com
      </p>
      <p class="contact-line">
        <svg viewBox="0 0 24 24"><path d="M12 2a10 10 0 1 0 0 20 10 10 0 0 0 0-20zm6.9 6h-3a15 15 0 0 0-1.3-3.9A8 8 0 0 1 18.9 8zM12 4c.8 1.1 1.5 2.5 1.9 4h-3.8c.4-1.5 1.1-2.9 1.9-4zM4.3 14a8 8 0 0 1 0-4h3.4a16 16 0 0 0 0 4zm.8 2h3a15 15 0 0 0 1.3 3.9A8 8 0 0 1 5.1 16zm3-8h-3a8 8 0 0 1 4.3-3.9A15 15 0 0 0 8.1 8zM12 20c-.8-1.1-1.5-2.5-1.9-4h3.8c-.4 1.5-1.1 2.9-1.9 4zm2.3-6H9.7a14 14 0 0 1 0-4h4.6a14 14 0 0 1 0 4zm.3 5.9a15 15 0 0 0 1.3-3.9h3a8 8 0 0 1-4.3 3.9zm1.7-5.9a16 16 0 0 0 0-4h3.4a8 8 0 0 1 0 4z"/></svg>
        www.brunnvollhaustechnik.com
      </p>
    </div>
  </section>
  <section class="card card-back">
    <div class="brand">
      <span class="brand-dot"></span>
      <span class="brand-name">Brunnvoll Haustechnik</span>
    </div>
  </section>
</main>
</body>
</html>
```